Save the date: email notification

I need a "Save the Date" email notification design for my wedding:

Objetives:

1.- to notify friends about our future wedding ( by sending an email)
2.- to request our friends to send us their phisical address. ( reply to the email)

It will not be the formal invitation for the wedding, just an announcement.

Wedding Date: 15-sep-2012
Our names: Lucía & Teodoro

Target Market(s)

friends, family and other commitments

Industry/Entity Type

Wedding

Requirements
Must have
• Wedding Date: 15-sep-2012
Our names: Lucía & Teodoro

```html
<!DOCTYPE html>
<html lang="en">
<head>
<meta charset="utf-8">
<title>Save the Date – Lucía &amp; Teodoro</title>
<link rel="stylesheet" href="https://fonts.googleapis.com/css2?family=Open+Sans:wght@400;700&amp;family=EB+Garamond:ital@1&amp;family=Parisienne&amp;display=swap">
<style>
  :root {
    --page: #ffffff;
    --card: #ede7da;
    --cocoa: #55271a;
    --ink: #4f2517;
  }
  * { margin: 0; padding: 0; box-sizing: border-box; }
  html, body {
    width: 1200px;
    height: 960px;
    overflow: hidden;
    background: var(--page);
  }
  .save-the-date {
    position: absolute;
    left: 24px;
    top: 146px;
    width: 1144px;
    height: 652px;
    background: var(--card);
  }
  .pattern-band {
    position: absolute;
    left: 0;
    top: 0;
    width: 271px;
    height: 100%;
    background: var(--cocoa);
  }
  .announcement {
    position: absolute;
    left: 271px;
    top: 0;
    right: 0;
    height: 100%;
    color: var(--ink);
    text-align: center;
  }
  .announcement > * {
    position: absolute;
    left: 0;
    right: 0;
  }
  .headline {
    top: 52px;
    font-family: "Open Sans", sans-serif;
    font-weight: 700;
    font-size: 50px;
    letter-spacing: 5px;
    margin-left: -14px;
  }
  .wedding-date {
    top: 152px;
    font-family: "EB Garamond", serif;
    font-style: italic;
    font-size: 40px;
    margin-left: -14px;
  }
  .couple {
    top: 222px;
    font-family: "Parisienne", cursive;
    font-size: 88px;
    font-weight: 400;
    margin-left: -14px;
  }
  .occasion {
    top: 446px;
    font-family: "Open Sans", sans-serif;
    font-size: 36px;
    margin-left: -14px;
  }
  .rsvp {
    top: 532px;
    font-family: "Open Sans", sans-serif;
    font-size: 22px;
    line-height: 34px;
    letter-spacing: 1.3px;
    margin-left: -14px;
  }
</style>
</head>
<body>
  <main class="save-the-date">
    <div class="pattern-band" role="img" aria-label="Decorative pattern of cream double rings on a chocolate brown band"></div>
    <section class="announcement">
      <h1 class="headline">SAVE THE DATE</h1>
      <p class="wedding-date">September 15, 2012</p>
      <h2 class="couple">Lucía &amp; Teodoro</h2>
      <p class="occasion">CELEBRATE OUR WEDDING</p>
      <p class="rsvp">R.S.V.P. to this email with your mailing address.<br>Soon we will send you our invitation.</p>
    </section>
  </main>
</body>
</html>
```